VELRO - Business cards

Business card to be created for Commercial sales staff

Target Market(s)

Commercial businesses

Industry/Entity Type

Commercial

Contact Information for Business Card

Look professional. For commercial clients

Colors
ffffff

Requirements
Must have
• - Velro Logo
• - Commercial sales staff as postion
• - room for commerical sales manager role
• - person name and their mobile number
• - Website : velropower.com.au
Nice to have
• White background.
• On back of business card just have the logo no other information
Should not have
• Should only have white background on front of card.

```html
<!DOCTYPE html>
<html lang="en">
<head>
<meta charset="utf-8">
<title>Velro – Business Cards</title>
<link rel="stylesheet" href="https://fonts.googleapis.com/css2?family=Open+Sans:wght@400;600;700;800&display=swap">
<style>
  :root {
    --backdrop: #ecebe8;
    --card: #ffffff;
    --ink: #111111;
    --brand-dark: #2f3138;
    --brand-red: #c8161d;
    --rule: #d9d9d9;
    --shadow: rgba(0, 0, 0, 0.18);
  }
  * { box-sizing: border-box; margin: 0; padding: 0; }
  html, body {
    width: 1200px;
    height: 872px;
    overflow: hidden;
    background: var(--backdrop);
    font-family: "Open Sans", Arial, sans-serif;
    color: var(--ink);
  }
  .canvas { position: relative; width: 1200px; height: 872px; }

  .card {
    position: absolute;
    width: 620px;
    height: 354px;
    background: var(--card);
    box-shadow: 0 14px 34px var(--shadow);
  }
  .card--back { left: 50px; top: 70px; display: flex; align-items: center; justify-content: center; }
  .card--front { left: 530px; top: 450px; }

  .wordmark { display: flex; align-items: center; gap: 16px; }
  .wordmark__dot { display: block; border-radius: 50%; background: var(--brand-red); }
  .wordmark__name {
    font-weight: 800;
    color: var(--brand-dark);
    letter-spacing: 0.02em;
    line-height: 1;
  }
  .card--back .wordmark__dot { width: 70px; height: 70px; }
  .card--back .wordmark__name { font-size: 104px; }

  .card--front .wordmark { position: absolute; left: 60px; top: 44px; gap: 8px; }
  .card--front .wordmark__dot { width: 24px; height: 24px; }
  .card--front .wordmark__name { font-size: 36px; }

  .contact {
    position: absolute;
    left: 42px;
    top: 150px;
    font-size: 16px;
    line-height: 30px;
  }
  .contact__label { font-weight: 700; }

  .divider {
    position: absolute;
    left: 348px;
    top: 120px;
    width: 2px;
    height: 200px;
    background: linear-gradient(to bottom, transparent, var(--rule) 20%, var(--rule) 80%, transparent);
  }

  .staff {
    position: absolute;
    left: 370px;
    top: 200px;
    width: 230px;
    text-align: center;
  }
  .staff__name { font-size: 34px; font-weight: 700; line-height: 1.1; }
  .staff__first { color: var(--brand-red); }
  .staff__last { color: var(--ink); }
  .staff__role { font-size: 18px; line-height: 22px; margin-top: 6px; }

  .website {
    position: absolute;
    left: 0;
    right: 0;
    bottom: 22px;
    text-align: center;
    font-size: 17px;
  }
</style>
</head>
<body>
<main class="canvas">
  <section class="card card--back" aria-label="Business card back">
    <div class="wordmark">
      <span class="wordmark__dot"></span>
      <span class="wordmark__name">VELRO</span>
    </div>
  </section>

  <section class="card card--front" aria-label="Business card front">
    <div class="wordmark">
      <span class="wordmark__dot"></span>
      <span class="wordmark__name">VELRO</span>
    </div>

    <div class="contact">
      <p><span class="contact__label">Phone:</span>&nbsp;&nbsp;&nbsp;0412-508-736</p>
      <p><span class="contact__label">Address:</span> 2140 Harlow Rd</p>
      <p>sales@velropower.com.au</p>
    </div>

    <div class="divider"></div>

    <div class="staff">
      <p class="staff__name"><span class="staff__first">Aaron</span> <span class="staff__last">Pell</span></p>
      <p class="staff__role">manager role<br>staff postion</p>
    </div>

    <p class="website">velropower.com.au</p>
  </section>
</main>
</body>
</html>
```